Join Wait / Reservations Handout

This is a handout for guests with information about the ability to join our
waitlist and/or make reservations. It will be handed out to any guest that ends up waiting on our waitlist to be seated. It will describe how our waitlist and reservations system works. It is informational for them to download our mobile app.

It was forcing me to move the look and feel sliders. Please refer to our branding guide for look and feel.

Industry/Entity Type

Hospitality

Contact Information for Business Card

One of the attached documents give a very generic layout of the information we need on this card. This layout is more for where we wanted the information placed and has nothing to do with the design aspects of the piece. Please use your imagination. Any of the 5 colors in the branding guide can be used anywhere. The pineapple design can be used anywhere in any color combination.

If you require any other files please let me know. Thanks

Other font styles liked:
• Please see attached branding guide

Requirements
Must have
• The only color requirement is that the logo be the blue with teal lettering...This has to match our app store logo.

```html
<!DOCTYPE html>
<html lang="en">
<head>
<meta charset="utf-8">
<title>Join Wait / Reservations Handout</title>
<link rel="stylesheet" href="https://fonts.googleapis.com/css2?family=Jost:wght@300;400&display=swap">
<style>
  :root {
    --page: #f4f2ee;
    --card: #0f3b47;
    --frame: #3f7580;
    --gold: #e2b143;
    --teal: #6fb9bd;
    --rose: #e39a86;
    --ink: #eef1ee;
    --rule-soft: #8fb7b9;
  }
  * { box-sizing: border-box; margin: 0; padding: 0; }
  html, body {
    width: 1200px;
    height: 756px;
    overflow: hidden;
    background: var(--page);
  }
  .canvas {
    width: 1200px;
    height: 756px;
    display: flex;
    align-items: center;
    justify-content: center;
  }
  .handout {
    width: 383px;
    height: 640px;
    background: var(--card);
    padding: 29px;
    font-family: "Jost", "Futura", sans-serif;
    font-weight: 300;
    box-shadow: 0 6px 18px rgba(15, 59, 71, 0.18);
  }
  .handout__frame {
    height: 100%;
    border: 1px solid var(--frame);
    display: flex;
    flex-direction: column;
    justify-content: space-evenly;
    padding: 20px 0 16px;
    align-items: center;
  }
  .info {
    width: 270px;
    display: flex;
    flex-direction: column;
    align-items: center;
    text-align: center;
  }
  .info--gold { color: var(--gold); }
  .info--teal { color: var(--teal); }
  .info--rose { color: var(--rose); }

  .rule {
    display: block;
    width: 100%;
    height: 8px;
    -webkit-mask-image: linear-gradient(to right, transparent, #000 18%, #000 82%, transparent);
    mask-image: linear-gradient(to right, transparent, #000 18%, #000 82%, transparent);
  }
  .rule path { fill: none; stroke: currentColor; stroke-width: 1; }
  .rule--plain { color: var(--rule-soft); opacity: 0.7; }

  .info__title {
    font-size: 17px;
    font-weight: 400;
    letter-spacing: 0.02em;
    text-transform: uppercase;
    margin: 9px 0 8px;
    line-height: 1;
  }
  .info__body {
    color: var(--ink);
    font-size: 16px;
    line-height: 1.4;
    margin: 12px 0 4px;
    font-weight: 400;
  }
  .info__note {
    color: var(--ink);
    font-size: 11px;
    margin: 0 0 4px;
    font-weight: 400;
  }
  .info__body + .rule, .info__note + .rule { margin-top: 10px; }
</style>
</head>
<body>
<main class="canvas">
  <article class="handout">
    <div class="handout__frame">

      <section class="info info--gold">
        <svg class="rule rule--plain" viewBox="0 0 270 8" preserveAspectRatio="none" aria-hidden="true"><path d="M0 4 H270"/></svg>
        <h2 class="info__title">When to join wait?</h2>
        <svg class="rule" viewBox="0 0 270 8" preserveAspectRatio="none" aria-hidden="true"><path d="M0 1.5 H126 L135 7 L144 1.5 H270"/></svg>
        <p class="info__body">Anytime</p>
        <svg class="rule rule--plain" viewBox="0 0 270 8" preserveAspectRatio="none" aria-hidden="true"><path d="M0 4 H270"/></svg>
      </section>

      <section class="info info--teal">
        <svg class="rule rule--plain" viewBox="0 0 270 8" preserveAspectRatio="none" aria-hidden="true"><path d="M0 4 H270"/></svg>
        <h2 class="info__title">When to reserve?</h2>
        <svg class="rule" viewBox="0 0 270 8" preserveAspectRatio="none" aria-hidden="true"><path d="M0 1.5 H126 L135 7 L144 1.5 H270"/></svg>
        <p class="info__body">Anytime- 2hours in Advance</p>
        <p class="info__note">(excluding weekend, open&nbsp; - 2pm)</p>
        <svg class="rule rule--plain" viewBox="0 0 270 8" preserveAspectRatio="none" aria-hidden="true"><path d="M0 4 H270"/></svg>
      </section>

      <section class="info info--teal">
        <svg class="rule rule--plain" viewBox="0 0 270 8" preserveAspectRatio="none" aria-hidden="true"><path d="M0 4 H270"/></svg>
        <h2 class="info__title">Sunday + Holiday Buffets</h2>
        <svg class="rule" viewBox="0 0 270 8" preserveAspectRatio="none" aria-hidden="true"><path d="M0 1.5 H126 L135 7 L144 1.5 H270"/></svg>
        <p class="info__body">Coming JUNE</p>
        <svg class="rule rule--plain" viewBox="0 0 270 8" preserveAspectRatio="none" aria-hidden="true"><path d="M0 4 H270"/></svg>
      </section>

      <section class="info info--rose">
        <svg class="rule rule--plain" viewBox="0 0 270 8" preserveAspectRatio="none" aria-hidden="true"><path d="M0 4 H270"/></svg>
        <h2 class="info__title">Large Groups</h2>
        <svg class="rule" viewBox="0 0 270 8" preserveAspectRatio="none" aria-hidden="true"><path d="M0 1.5 H126 L135 7 L144 1.5 H270"/></svg>
        <p class="info__body">Handled/Contacted by<br>Catering Manager</p>
        <svg class="rule rule--plain" viewBox="0 0 270 8" preserveAspectRatio="none" aria-hidden="true"><path d="M0 4 H270"/></svg>
      </section>

    </div>
  </article>
</main>
</body>
</html>
```